Informational Website for MOSVALEK-MOSaic VALley Eastern Kinship of Clinic Record Scholars

I need an informational website to help establish us as a legitimate entity. This will help us as we seek funding in to perform the research we intend to carry out. We are a newly formed group of family physicians and primary care researchers from 9 different countries around the world. We have access to electronic medical record data and/or health insurance claims data in our respective countries. We intend to perform international comparative studies in primary care. Our set of projects are to study the impact of the COVID-19 pandemic on primary care in our respective countries and around the world.
I've already purchased a domain and website from Wix. It is a premium account. The domain is https://www.mosvalekclinicnet.org

Target Market(s)

Researchers, policy makers, universities, research funding agencies

Coding

Coded - Design and coding required

Number of Pages Required

5+ page

Font styles to use
Sans Serif

Requirements
Must have
• Must have our logo and an interactive map of the world highlighting Canada, Australia, China (including Hong Kong), Norway, Singapore, South Korea, Sweden, United Kingdom, United States.
This map must be editable such that we can add or remove countries and cities as we evolve. Please see attached brief.
Nice to have
• Nice to depict primary care and big data research

```html
<!DOCTYPE html>
<html lang="en">
<head>
<meta charset="utf-8">
<title>MOSVALEK – MOSaic VALley Eastern Kinship of Clinic Record Scholars</title>
<link href="https://fonts.googleapis.com/css2?family=Jost:wght@400;500;600&family=Oswald:wght@400&display=swap" rel="stylesheet">
<style>
:root{
  --navy:#0e2d82;
  --navy-deep:#0f2a78;
  --green:#77a818;
  --sky:#c4d4e4;
  --white:#ffffff;
  --ink:#1b2d6b;
  --muted:#4a5575;
}
*{box-sizing:border-box;margin:0;padding:0}
html,body{width:1200px;height:2507px;overflow:hidden}
body{font-family:'Jost',sans-serif;color:var(--ink);background:var(--white);position:relative}

/* header */
.site-header{position:absolute;left:0;top:0;width:1200px;height:96px;background:var(--white);z-index:3}
.brand{position:absolute;left:88px;top:0;width:212px;height:135px;background:var(--white);border-radius:0 0 110px 110px / 0 0 40px 40px;z-index:4;display:flex;align-items:center;justify-content:center;gap:8px}
.brand-dot{width:20px;height:20px;border-radius:50%;background:var(--navy)}
.brand-name{font-weight:600;font-size:26px;color:var(--navy);letter-spacing:.5px}
.main-nav{position:absolute;top:41px;left:457px;display:flex;gap:34px;font-size:11.5px;font-weight:500;letter-spacing:.8px}
.main-nav a{color:var(--navy);text-decoration:none}
.main-nav a.is-active{color:var(--green)}
.header-call{position:absolute;left:818px;top:35px;font-family:'Oswald',sans-serif;font-size:17px;color:#222}
.header-call span{color:var(--green)}
.btn{display:flex;align-items:center;justify-content:center;font-size:11px;font-weight:500;letter-spacing:1px;color:var(--white);text-decoration:none;border-radius:3px}
.btn-navy{background:var(--navy)}
.btn-green{background:var(--green)}
.header-cta{position:absolute;left:984px;top:28px;width:128px;height:40px}

/* hero */
.hero{position:absolute;left:0;top:96px;width:1200px;height:480px;background:radial-gradient(ellipse 420px 260px at 180px 140px,#8a7b72 0%,rgba(138,123,114,0) 100%),linear-gradient(120deg,#93a2b6 0%,#7688a2 45%,#56677f 100%)}
.hero-title{position:absolute;left:88px;top:168px;font-size:30px;font-weight:600;line-height:39px;color:var(--white);width:620px}
.hero-cta{position:absolute;left:90px;top:267px;width:128px;height:40px}
.hero-dots{position:absolute;left:1094px;top:189px;display:flex;flex-direction:column;gap:12px}
.hero-dots i{width:17px;height:17px;border:1.5px solid var(--white);border-radius:50%;display:block;position:relative}
.hero-dots i.is-current::after{content:"";position:absolute;left:4px;top:4px;width:6px;height:6px;border-radius:50%;background:var(--white)}

/* about */
.about{position:absolute;left:0;top:576px;width:1200px;height:424px;background:var(--sky)}
.about-photo{position:absolute;left:88px;top:64px;width:496px;height:296px;background:radial-gradient(ellipse 180px 150px at 260px 170px,#d9d2c8 0%,rgba(217,210,200,0) 100%),linear-gradient(135deg,#4f6d34,#7f9a55 55%,#6d7d58)}
.section-heading{font-size:30px;font-weight:500;color:var(--navy);display:flex;align-items:center;gap:22px}
.rule{display:block;width:80px;height:2px;background:var(--green)}
.about-heading{position:absolute;left:640px;top:72px}
.about-lead{position:absolute;left:640px;top:128px;width:450px;font-size:14px;font-weight:500;line-height:19.5px;color:var(--navy)}
.about-lead em{font-style:normal;color:var(--green)}
.about-body{position:absolute;left:640px;top:205px;width:470px;font-size:13.5px;line-height:19.5px;color:var(--navy)}
.about-cta{position:absolute;left:640px;top:309px;width:144px;height:40px}

/* services */
.services{position:absolute;left:0;top:1000px;width:1200px;height:590px}
.services-heading{position:absolute;left:0;top:72px;width:1200px;justify-content:center}
.service-card{position:absolute;top:200px;width:320px;height:311px;border:2px solid var(--navy);border-radius:2px;text-align:center}
.service-card.is-featured{border-color:var(--green)}
.service-icon{position:absolute;left:98px;top:-58px;width:156px;height:110px;background:var(--white)}
.service-title{position:absolute;left:0;top:66px;width:100%;font-size:19px;font-weight:500;color:var(--navy)}
.is-featured .service-title{color:var(--green)}
.service-text{position:absolute;left:24px;top:108px;width:268px;font-size:11.5px;line-height:17.6px;color:var(--muted)}
.service-cta{position:absolute;left:102px;top:238px;width:112px;height:40px}

/* contact form */
.touch{position:absolute;left:0;top:1590px;width:1200px;height:433px;background:linear-gradient(180deg,#c9d7e6,#b6c8dc)}
.touch-heading{position:absolute;left:0;top:74px;width:1200px;justify-content:center}
.field{position:absolute;height:39px;background:var(--white);border-radius:2px;font-size:11.5px;color:#333;padding:12px 16px}
.field-message{height:95px}
.touch-submit{position:absolute;left:545px;top:312px;width:112px;height:39px}

/* footer */
.site-footer{position:absolute;left:0;top:2023px;width:1200px;height:484px;background:var(--navy-deep);color:var(--white)}
.footer-heading{position:absolute;left:88px;top:106px;font-size:28px;font-weight:500;color:var(--white);display:flex;align-items:center;gap:22px}
.footer-call{position:absolute;left:88px;top:150px;font-family:'Oswald',sans-serif;font-size:17px;display:flex;align-items:center;gap:6px}
.footer-mail{position:absolute;left:88px;top:176px;font-size:13px}
.footer-address{position:absolute;left:88px;top:213px;font-size:13.5px;line-height:19.5px}
.footer-address strong{font-weight:600}
.socials{position:absolute;left:88px;top:292px;display:flex;gap:7px}
.socials i{width:32px;height:32px;border:1.5px solid var(--green);border-radius:50%;display:block}
.socials i.is-hover{background:var(--green)}
.footer-map{position:absolute;left:616px;top:71px;width:496px;height:280px;background:linear-gradient(135deg,#eef0ee,#f4eddd 60%,#ecebe6);border-radius:3px}
.map-label{position:absolute;left:97px;top:94px;width:304px;height:56px;background:var(--white);color:var(--navy);font-size:13px;line-height:17px;text-align:center;padding:10px 8px;box-shadow:0 1px 4px rgba(0,0,0,.15)}
.map-pin{position:absolute;left:243px;top:170px}
.footer-rule{position:absolute;left:88px;top:399px;width:1024px;height:1px;background:rgba(255,255,255,.35)}
.copyright{position:absolute;left:88px;top:430px;font-size:13px}
.copyright span{color:var(--green)}
.footer-nav{position:absolute;left:616px;top:432px;display:flex;gap:30px;font-size:13px}
.footer-nav a{color:var(--white);text-decoration:none}
.to-top{position:absolute;left:1094px;top:428px}
</style>
</head>
<body>

<header class="site-header">
  <nav class="main-nav">
    <a class="is-active" href="#">HOME</a>
    <a href="#">ABOUT US</a>
    <a href="#">SERVICES</a>
    <a href="#">CONTACT US</a>
  </nav>
  <div class="header-call"><span>Call:</span> +100 55 01234</div>
  <a class="btn btn-navy header-cta" href="#">GET IN TOUCH</a>
</header>
<div class="brand"><span class="brand-dot"></span><span class="brand-name">MOSVALEK</span></div>

<section class="hero" role="img" aria-label="Doctor working at a desk with stethoscope, tablet and medical data overlay">
  <h1 class="hero-title">MOSaic VALley Eastern Kinship of Clinic Record Scholars</h1>
  <a class="btn btn-green hero-cta" href="#">CONTACT US</a>
  <div class="hero-dots"><i></i><i class="is-current"></i><i></i><i></i></div>
</section>

<section class="about">
  <div class="about-photo" role="img" aria-label="Family physician standing with a smiling family outdoors"></div>
  <h2 class="section-heading about-heading">About Us <span class="rule"></span></h2>
  <p class="about-lead">We are a group of family physicians and primary care health services researchers collaborating together to study the impact of the <em>COVID-19 pandemic on primary care around the world.</em></p>
  <p class="about-body">Lorem Ipsum is simply dummy text of the printing and typesetting industry. Lorem Ipsum has been the industry's standard dummy text ever since the 1500s, when an unknown printer took a galley of type and scrambled it to make a type specimen book ...</p>
  <a class="btn btn-navy about-cta" href="#">DISCOVER MORE</a>
</section>

<section class="services">
  <h2 class="section-heading services-heading"><span class="rule"></span>Services We Provide<span class="rule"></span></h2>

  <article class="service-card" style="left:88px">
    <svg class="service-icon" viewBox="0 0 156 110" fill="none" stroke="#0e2d82" stroke-width="3">
      <circle cx="60" cy="50" r="48"/>
      <path d="M36 50h12l6-12 8 24 6-12h14" stroke="#77a818" stroke-width="2.5"/>
    </svg>
    <h3 class="service-title">Primary Care</h3>
    <p class="service-text">It is a long established fact that a reader will be distracted by the readable content of a page when looking at its layout. The point of using Lorem Ipsum is that it has a more-or-less normal distribution of letters, as opposed There are many variations of passages of Lorem Ipsum available, ...</p>
    <a class="btn btn-navy service-cta" href="#">READ MORE</a>
  </article>

  <article class="service-card is-featured" style="left:440px">
    <svg class="service-icon" viewBox="0 0 156 110" fill="none" stroke="#77a818" stroke-width="3">
      <circle cx="60" cy="50" r="48"/>
      <path d="M42 66V46M54 66V38M66 66V50M78 66V32" stroke-width="4"/>
    </svg>
    <h3 class="service-title">Big Data Research</h3>
    <p class="service-text">It is a long established fact that a reader will be distracted by the readable content of a page when looking at its layout. The point of using Lorem Ipsum is that it has a more-or-less normal distribution of letters, as opposed There are many variations of passages of Lorem Ipsum available, ...</p>
    <a class="btn btn-green service-cta" href="#">READ MORE</a>
  </article>

  <article class="service-card" style="left:792px">
    <svg class="service-icon" viewBox="0 0 156 110" fill="none" stroke="#0e2d82" stroke-width="3">
      <circle cx="60" cy="50" r="48"/>
      <circle cx="60" cy="50" r="22" stroke="#77a818" stroke-width="2.5"/>
      <path d="M38 50h44M60 28c-10 12-10 32 0 44M60 28c10 12 10 32 0 44" stroke="#77a818" stroke-width="2"/>
    </svg>
    <h3 class="service-title">International</h3>
    <p class="service-text">It is a long established fact that a reader will be distracted by the readable content of a page when looking at its layout. The point of using Lorem Ipsum is that it has a more-or-less normal distribution of letters, as opposed There are many variations of passages of Lorem Ipsum available, ...</p>
    <a class="btn btn-navy service-cta" href="#">READ MORE</a>
  </article>
</section>

<section class="touch" role="img" aria-label="Soft-focus laptop and medical paperwork on a desk">
  <h2 class="section-heading touch-heading"><span class="rule"></span>Get in Touch With Us<span class="rule"></span></h2>
  <div class="field" style="left:208px;top:138px;width:247px">Your Name</div>
  <div class="field" style="left:476px;top:138px;width:247px">Email</div>
  <div class="field" style="left:744px;top:138px;width:248px">Subject</div>
  <div class="field field-message" style="left:208px;top:197px;width:784px">Message ...</div>
  <a class="btn btn-green touch-submit" href="#">SUBMIT</a>
</section>

<footer class="site-footer">
  <h2 class="footer-heading">Contact Us <span class="rule"></span></h2>
  <div class="footer-call">Call Us:
    <svg width="16" height="16" viewBox="0 0 24 24" fill="none" stroke="#fff" stroke-width="2"><path d="M5 3h4l2 5-3 2a12 12 0 0 0 6 6l2-3 5 2v4a2 2 0 0 1-2 2A17 17 0 0 1 3 5a2 2 0 0 1 2-2z"/></svg>
    +100-555-0148</div>
  <div class="footer-mail">Email: contact@mosvalekclinicnet.org</div>
  <p class="footer-address"><strong>Department of Family and Community Medicine<br>Valley Crest University</strong><br>210 Orchard Lane, 4th Floor Brookvale, ON, Canada, K0A 9Z9</p>
  <div class="socials" aria-label="Social links"><i></i><i class="is-hover"></i><i></i></div>

  <div class="footer-map" role="img" aria-label="Street map around the office location">
    <div class="map-label">210 Orchard Lane, 4th Floor Brookvale,<br>ON, Canada, K0A 9Z9</div>
    <svg class="map-pin" width="22" height="30" viewBox="0 0 22 30"><path d="M11 0a11 11 0 0 1 11 11c0 8-11 19-11 19S0 19 0 11A11 11 0 0 1 11 0z" fill="#e53935"/><circle cx="11" cy="11" r="4" fill="#9b1b1b"/></svg>
  </div>

  <div class="footer-rule"></div>
  <p class="copyright">© 2021 <span>MOSVALEK</span>. All Rights Reseved</p>
  <nav class="footer-nav"><a href="#">Home</a><a href="#">About Us</a><a href="#">Services</a><a href="#">Contact Us</a></nav>
  <svg class="to-top" width="18" height="20" viewBox="0 0 18 20" fill="none" stroke="#77a818" stroke-width="2"><path d="M9 2L2 18h14z"/><path d="M9 9v6"/></svg>
</footer>

</body>
</html>
```